KTR Engineering Business Card Design

We’re looking for an elegant, clean, and timeless business card design that communicates experience, capability, and reliability.

KTR Engineering was established in 1995 , we are a Government Contracting company providing Professional Services to the Ministry of Harbor Works, Frontier Stewardship and the Waypoint Consortium. Our capabilities include: Acquisition & Program Management; Intelligence & Security Operations; Cyber, IT & Network Operations; Lifecycle Logistics & Asset Readiness; C5ISR Systems Engineering & Sustainment.

We want the card to reflect a straightforward, confident approach to business. The design should feel polished and professional without being flashy or overly corporate.

Design Direction
Clean, sophisticated, and uncluttered
Elegant but understated
Strong typography and thoughtful spacing
A timeless aesthetic rather than something overly trendy
Confident and established, with a sense of substance
Easy to read and practical in a real-world business setting

The overall impression should be: “These are experienced professionals who know what they’re doing, do what they say, and can be relied upon.”

We’re open to creative interpretations. The finished card should feel distinctive through its typography, proportions, layout, and attention to detail rather than through excessive graphics or visual effects.

We’re looking for a design that would make a potential client immediately feel that they’re dealing with a capable, trustworthy, and established company.

Company Colors: Navy and Gold/Yellow (but you do not need to use these colors on the card)
Company Name: KTR Engineering Associates, Inc. (known as KTR Engineering)
Website: ktrengineering.example
Company Logo: Navy & Gold (other variations attached)

```html
<!DOCTYPE html>
<html lang="en">
<head>
<meta charset="utf-8">
<title>KTR Engineering – Business Card</title>
<link href="https://fonts.googleapis.com/css2?family=Source+Sans+3:ital,wght@0,400;0,700;0,800;1,400&display=swap" rel="stylesheet">
<style>
  :root {
    --navy: #0d1240;
    --gold: #fde24f;
    --white: #ffffff;
    --backdrop: #e8e8e8;
  }
  * { margin: 0; padding: 0; box-sizing: border-box; }
  html, body {
    width: 1200px; height: 960px; overflow: hidden;
    background: var(--backdrop);
    font-family: "Source Sans 3", sans-serif;
  }
  .canvas { position: relative; width: 1200px; height: 960px; }
  .card {
    position: absolute; width: 752px; height: 430px;
    background: var(--navy); overflow: hidden;
  }
  .card--front { left: 130px; top: 50px; }
  .card--back { left: 345px; top: 508px; }

  .wordmark {
    position: absolute; color: var(--white);
    font-weight: 800; letter-spacing: 1px; line-height: 1;
  }
  .card--front .wordmark { left: 78px; top: 72px; font-size: 88px; }
  .card--back .wordmark { left: 216px; top: 168px; font-size: 140px; }

  .person { position: absolute; left: 40px; top: 214px; }
  .person__name { color: var(--gold); font-weight: 700; font-size: 29px; line-height: 1.1; }
  .person__title { color: var(--white); font-style: italic; font-size: 18px; margin-top: 2px; }

  .divider {
    position: absolute; left: 0; top: 280px; width: 100%; height: 5px;
    background: var(--gold);
  }

  .contact { position: absolute; left: 40px; top: 296px; list-style: none; }
  .contact__item {
    display: flex; align-items: center; height: 24px;
    color: var(--white); font-size: 18.5px;
  }
  .contact__item--address { height: 30px; margin-bottom: 3px; }
  .contact__icon { width: 20px; height: 20px; margin-right: 16px; flex: none; }
  .contact__item--address .contact__icon { height: 26px; }
</style>
</head>
<body>
<main class="canvas">
  <section class="card card--front">
    <div class="wordmark">KTR</div>
    <div class="person">
      <p class="person__name">Person Name</p>
      <p class="person__title">Director</p>
    </div>
    <div class="divider"></div>
    <ul class="contact">
      <li class="contact__item contact__item--address">
        <svg class="contact__icon" viewBox="0 0 20 26"><path d="M10 1C5.6 1 2.5 4.3 2.5 8.4 2.5 14 10 25 10 25s7.5-11 7.5-16.6C17.5 4.3 14.4 1 10 1z" fill="var(--gold)"/><circle cx="10" cy="8.5" r="3" fill="var(--navy)"/></svg>
        4120 Harbor Point Avenue, Suite 310, Bayview, VA 23999
      </li>
      <li class="contact__item">
        <svg class="contact__icon" viewBox="0 0 20 20"><path d="M4 2l3 3.5-1.6 2.2c1.2 2.6 3.2 4.6 5.8 5.8L13.4 12 17 15l-1.8 3C8.5 17.5 2.5 11.5 2 4.8z" fill="var(--gold)"/><path d="M12 2.5a6 6 0 0 1 5.5 5.5M12 5.5a3 3 0 0 1 2.5 2.5" stroke="var(--gold)" stroke-width="1.5" fill="none"/></svg>
        555-201-4783
      </li>
      <li class="contact__item">
        <svg class="contact__icon" viewBox="0 0 20 20"><path d="M1 8l9-6 9 6v10H1z" fill="var(--gold)"/><path d="M1 8l9 6 9-6" stroke="var(--navy)" stroke-width="1.4" fill="none"/></svg>
        info@ktrengineering.example
      </li>
      <li class="contact__item">
        <svg class="contact__icon" viewBox="0 0 20 20" fill="none" stroke="var(--gold)" stroke-width="1.3"><circle cx="10" cy="10" r="8"/><ellipse cx="10" cy="10" rx="3.5" ry="8"/><path d="M2 10h16M3.5 6h13M3.5 14h13"/></svg>
        www.ktrengineering.example
      </li>
    </ul>
  </section>

  <section class="card card--back">
    <div class="wordmark">KTR</div>
  </section>
</main>
</body>
</html>
```